Harrowfen Logistics, Project

Company Profile
Harrowfen Logistics Sdn Bhd is a well established and experienced freight forwarder in Kuala Lumpur, Malaysia. We specialize in air and sea forwarding, Custom Brokerage and regulatory compliance services, inland transportation,
overseas freighting and warehousing and distribution management. With our dedicated qualified and experienced professionals, we are fully committed to serving our clients.

Our Mission
Based on the motto “Quick, Reliable and Polite”, Harrowfen Logistics is dedicated to upholding the following three points corporate philosophy:
1. Adhering to the principle that “the customer always comes first”.
2. Contributing to the development of the local community.
3. Making it our duty to be responsible and sincere.

Our Edge
• One-Stop Logistics Solutions
• Extensive Network Throughout Malaysia
• Highly Qualified and Experienced Pool of Professionals
• Comprehensive IT Solutions
• Innovative and Customer-focused Solutions
• Flexible and Consistent in Managing Exceptions
• Total Supply Chain Visibility

Target Market(s)

We sell the logistics services to all the industry in Malaysia. (ONE Stop Logistics Solutions)

Industry/Entity Type

Logistic

Contact Information for Business Card

I want the back of the card to be white with the logo and slogan. i would like to see the logo on the front with the general info.

Requirements
Must have
• Name, Title, Office, Cell, Fax, Email, Address, Website
Nice to have
• Modern Design Business Card

```html
<!DOCTYPE html>
<html lang="en">
<head>
<meta charset="utf-8">
<title>Harrowfen Logistics – Stationery</title>
<link rel="stylesheet" href="https://fonts.googleapis.com/css2?family=Open+Sans:wght@400;600;700;800&family=Roboto:wght@400;500&display=swap">
<style>
  :root{
    --bg:#1e1e1e;
    --blue:#1d8fd8;
    --blue-light:#29a8e6;
    --blue-deep:#1a6fbd;
    --ink:#2b2b2b;
    --grey:#8a8a8a;
    --paper:#ffffff;
  }
  *{box-sizing:border-box;margin:0;padding:0}
  html,body{width:1200px;height:780px;overflow:hidden;background:var(--bg)}
  body{position:relative;font-family:"Open Sans",Arial,sans-serif;color:var(--ink)}

  .sheet{position:absolute;overflow:hidden}
  .band{position:absolute;left:0;bottom:0;width:100%;display:block}

  .wordmark{font-family:"Open Sans",Arial,sans-serif;font-weight:700;color:var(--blue);white-space:nowrap;line-height:1.1}
  .wordmark.on-blue{color:#fff}
  .wordmark .dot{display:inline-block;width:.55em;height:.55em;border-radius:50%;background:currentColor;margin-right:.35em;vertical-align:.05em}

  /* folder cover */
  .folder{left:40px;top:130px;width:320px;height:452px;background:linear-gradient(170deg,var(--blue-light),var(--blue-deep));display:flex;align-items:center;justify-content:center}
  .folder .wordmark{font-size:22px}

  /* letterhead */
  .letterhead{left:390px;top:150px;width:340px;height:481px;background:var(--paper)}
  .letterhead .wordmark{position:absolute;left:24px;top:40px;font-size:13px}
  .lh-address{position:absolute;right:22px;top:22px;width:150px;font-size:5.2px;line-height:1.45;color:var(--ink);font-style:normal}
  .lh-address .co{color:var(--blue);font-weight:700}
  .lh-address .lbl{color:var(--blue);font-weight:700}
  .lh-rule{position:absolute;left:24px;right:22px;top:74px;border-top:1px solid #555}
  .lh-body{position:absolute;left:24px;right:26px;top:100px;font-family:"Roboto",Arial,sans-serif;font-size:6.6px;line-height:1.75;color:#444}
  .lh-body p{margin-bottom:9px}
  .lh-sign{position:absolute;right:40px;top:330px;font-family:"Roboto",Arial,sans-serif;font-size:6.4px;letter-spacing:.5px;color:#555}

  /* cards */
  .card{width:195px;height:112px}
  .card-front{background:var(--paper)}
  .card-back{background:linear-gradient(170deg,var(--blue-light),var(--blue-deep));color:#fff}
  .card-front .wordmark{position:absolute;left:10px;top:38px;width:62px;font-size:9px;white-space:normal;line-height:1.15}
  .cf-person{position:absolute;left:76px;right:6px;top:7px;font-size:4.8px;line-height:1.4;white-space:nowrap}
  .cf-person .name{font-size:7.5px;font-weight:700;color:var(--blue);line-height:1.2}
  .cf-person .title{font-size:4.8px;color:var(--ink)}
  .cf-person .co{margin-top:3px;color:var(--blue);font-weight:700}
  .cf-person .lbl{color:var(--blue);font-weight:700}
  .slogan{position:absolute;font-weight:800;text-transform:uppercase;letter-spacing:.3px;color:#fff;line-height:1;white-space:nowrap}
  .card-front .slogan{left:58px;bottom:2.5px;font-size:4.8px}

  .cb-title{position:absolute;left:12px;top:12px;font-size:5.4px;font-weight:700}
  .cb-list{position:absolute;top:20px;list-style:none;font-size:4.6px;line-height:1.5}
  .cb-list li::before{content:"";display:inline-block;width:2.5px;height:2.5px;background:#fff;border-radius:50%;margin-right:3px;vertical-align:1px}
  .cb-list.left{left:12px}
  .cb-list.right{left:108px;top:10px}
  .card-back .wordmark{position:absolute;left:104px;top:62px;font-size:7px}
  .card-back .slogan{right:12px;bottom:10px;font-size:5.4px}

  /* envelope */
  .envelope{left:760px;top:410px;width:404px;height:200px;background:var(--paper)}
  .envelope .wordmark{position:absolute;left:50%;top:78px;transform:translateX(-50%);font-size:20px}
</style>
</head>
<body>

<svg width="0" height="0" style="position:absolute">
  <defs>
    <linearGradient id="greyFade" x1="0" x2="1" y1="0" y2="0">
      <stop offset="0" stop-color="#6e6e6e"/>
      <stop offset="1" stop-color="#e6e6e6"/>
    </linearGradient>
    <symbol id="footerBand" viewBox="0 0 100 10" preserveAspectRatio="none">
      <polygon points="0,6 77,6 79,0 83,0 81,10 0,10" fill="#1d8fd8"/>
      <polygon points="83,0 100,0 100,10 81,10" fill="url(#greyFade)"/>
    </symbol>
    <symbol id="cardBand" viewBox="0 0 100 10" preserveAspectRatio="none">
      <polygon points="0,0 80,0 78,10 0,10" fill="#1d8fd8"/>
      <polygon points="82,0 100,0 100,10 80,10" fill="url(#greyFade)"/>
    </symbol>
  </defs>
</svg>

<!-- folder cover -->
<section class="sheet folder">
  <span class="wordmark on-blue"><span class="dot"></span>Harrowfen Logistics</span>
</section>

<!-- letterhead -->
<section class="sheet letterhead">
  <span class="wordmark">Harrowfen Logistics</span>
  <address class="lh-address">
    <div class="co">HARROWFEN LOGISTICS SDN BHD (1234567-A)</div>
    <div>No. 12B, 2nd Floor, Jalan Seri Permai 3,</div>
    <div>Taman Seri Permai, 41050 Klang,</div>
    <div>Selangor Darul Ehsan, Malaysia.</div>
    <div><span class="lbl">Email:</span> enquiry@harrowfen.com.my</div>
    <div><span class="lbl">Tel:</span> (603) 5550 2180</div>
    <div><span class="lbl">Fax:</span> (603) 5550 2190</div>
    <div><span class="lbl">GST Registration No:</span> 000123456789</div>
  </address>
  <div class="lh-rule"></div>
  <div class="lh-body">
    <p>Lorem Ipsum is simply dummy text of the printing and typesetting industry. Lorem Ipsum has been the industry's standard dummy text ever since the 1500s, when an unknown printer took a galley of type and scrambled it to make a type specimen book. It has survived not only five centuries, but also the leap into electronic typesetting, remaining essentially unchanged. It was popularised in the 1960s with the release of Letraset sheets containing Lorem Ipsum passages, and more recently with desktop publishing software like Aldus PageMaker including versions of Lorem Ipsum.</p>
    <p>It is a long established fact that a reader will be distracted by the readable content of a page when looking at its layout. The point of using Lorem Ipsum is that it has a more-or-less normal distribution of letters, as opposed to using 'Content here, content here', making it look like readable English.</p>
    <p>Many desktop publishing packages and web page editors now use Lorem Ipsum as their default model text, and a search for 'lorem ipsum' will uncover many web sites still in their infancy. Various versions have evolved over the years, sometimes by accident, sometimes on purpose (injected humour and the like).</p>
  </div>
  <div class="lh-sign">NADIRA HASHIM</div>
  <svg class="band" height="18"><use href="#footerBand" width="100%" height="100%"/></svg>
</section>

<!-- business card backs (blue) -->
<section class="sheet card card-back" style="left:760px;top:150px">
  <div class="cb-title">We're Specialise In:</div>
  <ul class="cb-list left">
    <li>International Shipping (Air/Sea)</li>
    <li>Transportation (Haulage)</li>
    <li>Consolidation - NVOCC</li>
    <li>Warehousing</li>
    <li>Project Management</li>
    <li>Packing</li>
  </ul>
  <ul class="cb-list right">
    <li>Supply Chain Management</li>
    <li>Marine Insurance</li>
    <li>Tax Exemption Consultancy</li>
    <li>Distribution</li>
    <li>Custom Brokerage</li>
    <li>Door to Door</li>
  </ul>
  <span class="wordmark on-blue">Harrowfen Logistics</span>
  <div class="slogan">One Stop Logistics Solutions</div>
</section>

<section class="sheet card card-back" style="left:969px;top:280px">
  <div class="cb-title">We're Specialise In:</div>
  <ul class="cb-list left">
    <li>International Shipping (Air/Sea)</li>
    <li>Transportation (Haulage)</li>
    <li>Consolidation - NVOCC</li>
    <li>Warehousing</li>
    <li>Project Management</li>
    <li>Packing</li>
  </ul>
  <ul class="cb-list right">
    <li>Supply Chain Management</li>
    <li>Marine Insurance</li>
    <li>Tax Exemption Consultancy</li>
    <li>Distribution</li>
    <li>Custom Brokerage</li>
    <li>Door to Door</li>
  </ul>
  <span class="wordmark on-blue">Harrowfen Logistics</span>
  <div class="slogan">One Stop Logistics Solutions</div>
</section>

<!-- business card fronts (white) -->
<section class="sheet card card-front" style="left:969px;top:150px">
  <span class="wordmark">Harrowfen Logistics</span>
  <div class="cf-person">
    <div class="name">Faris Azlan</div>
    <div class="title">Managing Director</div>
    <div><span class="lbl">Tel:</span> +6012-555 0142</div>
    <div class="co">HARROWFEN LOGISTICS SDN BHD (1234567-A)</div>
    <div>No. 12B, 2nd Floor, Jalan Seri Permai 3,</div>
    <div>Taman Seri Permai, 41050 Klang,</div>
    <div>Selangor Darul Ehsan, Malaysia.</div>
    <div><span class="lbl">Email:</span> faris.azlan@harrowfen.com.my</div>
    <div><span class="lbl">Tel:</span> (603) 5550 2180 / 2181</div>
    <div><span class="lbl">Fax:</span> (603) 5550 2190</div>
    <div><span class="lbl">Website:</span> www.harrowfen.com.my</div>
  </div>
  <svg class="band" height="10"><use href="#cardBand" width="100%" height="100%"/></svg>
  <div class="slogan">One Stop Logistics Solutions</div>
</section>

<section class="sheet card card-front" style="left:760px;top:280px">
  <span class="wordmark">Harrowfen Logistics</span>
  <div class="cf-person">
    <div class="name">Faris Azlan</div>
    <div class="title">Managing Director</div>
    <div><span class="lbl">Tel:</span> +6012-555 0142</div>
    <div class="co">HARROWFEN LOGISTICS SDN BHD (1234567-A)</div>
    <div>No. 12B, 2nd Floor, Jalan Seri Permai 3,</div>
    <div>Taman Seri Permai, 41050 Klang,</div>
    <div>Selangor Darul Ehsan, Malaysia.</div>
    <div><span class="lbl">Email:</span> faris.azlan@harrowfen.com.my</div>
    <div><span class="lbl">Tel:</span> (603) 5550 2180 / 2181</div>
    <div><span class="lbl">Fax:</span> (603) 5550 2190</div>
    <div><span class="lbl">Website:</span> www.harrowfen.com.my</div>
  </div>
  <svg class="band" height="10"><use href="#cardBand" width="100%" height="100%"/></svg>
  <div class="slogan">One Stop Logistics Solutions</div>
</section>

<!-- envelope -->
<section class="sheet envelope">
  <span class="wordmark">Harrowfen Logistics</span>
  <svg class="band" height="20"><use href="#footerBand" width="100%" height="100%"/></svg>
</section>

</body>
</html>
```